Leaflet to promote a new sports massage business

I am a Remedial and Sports Massage therapist and treat a range of people from professionals who spend hours working behind computers and have associated neck and back pain through poor posture to amateur sports people of varying intensity/ability - who encounter injuries along the way, or just need some good old stretching out.Remedial and sports massage helps people who have musculoskeletal injury, pain or dysfunction brought about by the stresses and strains of life. Through massage i can reduce pain, promote recovery after injury, relieve stress, and improve flexibility. All of this contributes to helping people feel better. I have just started working at a new location (address attached) and am looking to raise awareness that I am there and to promote the benefits of massage to encourage new clients(attached as a separate document). I have a business card (attached to the brief) which uses hands as the main device, I would like to include these – possibly in some sort of logo and I would like to use purple as a key colour (if colour is used). I also want to include the KVTB logo (attached) to add credibility

```html
<!DOCTYPE html>
<html lang="en">
<head>
<meta charset="utf-8">
<title>Rosalind Ashby – Remedial and Sports Massage Leaflet</title>
<link href="https://fonts.googleapis.com/css2?family=Roboto+Condensed:wght@700&family=Open+Sans:wght@300;400&family=Lato:wght@300;400;700&family=Marcellus&display=swap" rel="stylesheet">
<style>
  :root {
    --purple-deep: #5a0f58;
    --purple-name: #9a5aa6;
    --purple-text: #6a1c6a;
    --blue-rule: #2a9bd3;
    --grey-sub: #555555;
    --ink: #222222;
    --white: #ffffff;
    --backdrop: #4a3a30;
    --skin-light: #f3e3d6;
    --skin-mid: #d9b49a;
    --skin-dark: #b98c6f;
  }
  * { box-sizing: border-box; margin: 0; padding: 0; }
  html, body { width: 1200px; height: 964px; overflow: hidden; }
  body { background: var(--backdrop); position: relative; }

  .leaflet {
    position: absolute; left: 105px; top: 137px;
    width: 990px; height: 696px;
    background: var(--white);
    overflow: hidden;
  }

  /* Header */
  .header-photo {
    position: absolute; left: 515px; top: 0; width: 475px; height: 251px;
    background: linear-gradient(90deg, rgba(255,255,255,1) 0%, rgba(243,227,214,0.6) 18%, var(--skin-light) 30%, var(--skin-mid) 65%, var(--skin-light) 100%);
  }
  .therapist-name {
    position: absolute; left: 50px; top: 30px;
    font-family: "Roboto Condensed", "Arial Narrow", sans-serif;
    font-weight: 700; font-size: 62px; letter-spacing: 1px;
    color: var(--purple-name); line-height: 1;
  }
  .therapist-role {
    position: absolute; left: 50px; top: 114px;
    font-family: "Open Sans", Arial, sans-serif;
    font-weight: 300; font-size: 50px; line-height: 60px;
    color: var(--grey-sub); letter-spacing: -0.8px;
  }

  .rule { position: absolute; left: 0; width: 990px; height: 4px; background: var(--blue-rule); }
  .rule--top { top: 251px; }
  .rule--bottom { top: 483px; }

  /* Middle band */
  .band {
    position: absolute; left: 0; top: 255px; width: 990px; height: 228px;
    background: var(--purple-deep);
  }
  .intro {
    position: absolute; left: 29px; top: 9px; width: 204px;
    font-family: "Lato", Arial, sans-serif; font-size: 12.7px; line-height: 19px;
    color: var(--white); text-align: justify;
  }
  .band-photo {
    position: absolute; left: 253px; top: 0; width: 328px; height: 228px;
    background: linear-gradient(135deg, var(--skin-light) 0%, var(--skin-mid) 50%, var(--skin-dark) 100%);
  }
  .benefits-tab {
    position: absolute; left: 510px; top: 0; width: 290px; height: 32px;
  }
  .benefits-tab span {
    position: absolute; left: 25px; top: 5px;
    font-family: "Lato", Arial, sans-serif; font-weight: 700; font-size: 19px;
    color: #111; letter-spacing: 0.2px;
  }
  .benefits {
    position: absolute; right: 34px; top: 39px; list-style: none;
    font-family: "Lato", Arial, sans-serif; font-weight: 700; font-size: 20.5px;
    color: var(--white); text-align: right;
  }
  .benefits li { height: 35.5px; display: flex; justify-content: flex-end; align-items: center; gap: 14px; }
  .benefits svg { width: 26px; height: 24px; }

  /* Footer */
  .hands-art {
    position: absolute; left: 0; top: 503px; width: 225px; height: 180px;
    background: linear-gradient(160deg, var(--purple-deep), #7b3a7a);
    border-radius: 40% 55% 0 0;
  }
  .affiliation {
    position: absolute; left: 190px; top: 515px; width: 140px; height: 80px;
    display: flex; align-items: center; gap: 8px;
  }
  .affiliation i { width: 26px; height: 26px; border-radius: 50%; background: var(--blue-rule); flex: none; }
  .affiliation span {
    font-family: "Lato", Arial, sans-serif; font-weight: 400; font-size: 20px;
    color: var(--purple-deep); letter-spacing: 3px;
  }
  .clinic {
    position: absolute; right: 40px; top: 502px;
    font-family: "Marcellus", Georgia, serif; font-size: 37px; color: var(--grey-sub);
  }
  .phone {
    position: absolute; right: 40px; top: 562px;
    font-family: "Lato", Arial, sans-serif; font-weight: 700; font-size: 34px; color: var(--ink);
  }
  .address {
    position: absolute; right: 40px; top: 611px;
    font-family: "Lato", Arial, sans-serif; font-size: 17px; color: var(--ink);
  }
  .address .label { font-weight: 300; font-size: 23px; color: var(--purple-text); margin-right: 4px; }
  .contacts {
    position: absolute; right: 42px; top: 651px;
    display: flex; align-items: center;
    font-family: "Lato", Arial, sans-serif; font-size: 19px; color: var(--purple-text);
  }
  .contacts .dot { width: 28px; height: 28px; border-radius: 50%; background: #2f5aa0; margin-right: 8px; }
  .contacts .email { font-weight: 700; font-size: 19.5px; margin-left: 20px; }
  .base-strip { position: absolute; left: 0; bottom: 0; width: 990px; height: 13px; background: var(--purple-deep); }
</style>
</head>
<body>
  <main class="leaflet">
    <header>
      <div class="header-photo" role="img" aria-label="Photo of a therapist's hands massaging a smiling client's shoulders"></div>
      <h1 class="therapist-name">ROSALIND ASHBY</h1>
      <p class="therapist-role">Remedial and sports<br>massage therapist</p>
    </header>

    <div class="rule rule--top"></div>

    <section class="band">
      <p class="intro">I am a Remedial and Sports Massage therapist and treat a range of people from professionals who spend hours working behind computers and have associated neck and back pain through poor posture to amateur sports people of varying intensity/ability - who encounter injuries along the way, or just need some good old stretching out.</p>
      <div class="band-photo" role="img" aria-label="Close-up photo of hands working on a client's back muscles"></div>
      <div class="benefits-tab">
        <svg width="290" height="32" viewBox="0 0 290 32"><path d="M0 0 H290 L274 32 H14 Z" fill="var(--blue-rule)"/></svg>
        <span>BENEFITS OF MASSAGE</span>
      </div>
      <ul class="benefits">
        <li>Reduces pain <svg viewBox="0 0 26 24"><path d="M2 13 L9 20 L24 3" fill="none" stroke="#fff" stroke-width="4" stroke-linecap="round" stroke-linejoin="round"/></svg></li>
        <li>Promotes recovery <svg viewBox="0 0 26 24"><path d="M2 13 L9 20 L24 3" fill="none" stroke="#fff" stroke-width="4" stroke-linecap="round" stroke-linejoin="round"/></svg></li>
        <li>Improves posture and flexibility <svg viewBox="0 0 26 24"><path d="M2 13 L9 20 L24 3" fill="none" stroke="#fff" stroke-width="4" stroke-linecap="round" stroke-linejoin="round"/></svg></li>
        <li>Relieves stress <svg viewBox="0 0 26 24"><path d="M2 13 L9 20 L24 3" fill="none" stroke="#fff" stroke-width="4" stroke-linecap="round" stroke-linejoin="round"/></svg></li>
        <li>Improves health and wellbeing <svg viewBox="0 0 26 24"><path d="M2 13 L9 20 L24 3" fill="none" stroke="#fff" stroke-width="4" stroke-linecap="round" stroke-linejoin="round"/></svg></li>
      </ul>
    </section>

    <div class="rule rule--bottom"></div>

    <footer>
      <div class="hands-art" role="img" aria-label="Illustration of two overlapping purple hands"></div>
      <div class="affiliation"><i></i><span>KVTB</span></div>
      <p class="clinic">Peak Motion Clinic</p>
      <p class="phone">Phone: 07700 900123</p>
      <p class="address"><span class="label">Address:</span>Elmfield Sports Ground, Mill Lane, Ashworth, AB1 2CD</p>
      <p class="contacts"><span class="dot"></span>linkhub.com/RosalindAshbyMassage<span class="email">rosalindashby@mailbox.com</span></p>
      <div class="base-strip"></div>
    </footer>
  </main>
</body>
</html>
```